Removals & Storage a5 brochure required

We require a a4 1 fold into a5 brochure designed. we are an established removals and storage company based in southport, uk. we are looking for somthing we can take into more corporate offices ( estate agents etc) to show off what we do. our website has alot of information : www.haul-and-keep.co.uk which may be of use. we offer Domestic and Commercial removals & storage, packaging sales and services, 24/7 self storage options, mobile self storage. archive storage etc etc i have many files like logos etc where required. nice clean images / hgv with our image superimposed
Target Market(s)
Corporate, estate agents, domestic removals,
Colors
Designer to choose colors to be used in the design.

```html
<!DOCTYPE html>
<html lang="en">
<head>
<meta charset="utf-8">
<title>Harbourside Removals and Storage – Brochure</title>
<link rel="stylesheet" href="https://fonts.googleapis.com/css2?family=Oswald:wght@700&family=Fira+Sans:wght@300;400;500&display=swap">
<style>
:root{
  --yellow:#f5bb0f;
  --yellow-deep:#e0a80a;
  --charcoal:#2e2e2e;
  --charcoal-soft:#3a3a3a;
  --ink:#3b3b3b;
  --white:#ffffff;
}
*{margin:0;padding:0;box-sizing:border-box}
html,body{width:1200px;height:928px;overflow:hidden;background:var(--white)}
body{font-family:"Fira Sans",sans-serif;font-weight:300;color:var(--ink);position:relative}
.abs{position:absolute}
.display{font-family:"Oswald",sans-serif;font-weight:700;color:var(--yellow);line-height:1;letter-spacing:-0.2px}

/* Left spread */
.hero-photo{left:0;top:0;width:600px;height:282px;background:linear-gradient(120deg,#3c3c3c 0%,#333 45%,#2b2b2b 100%)}
.hero-band{left:0;top:0;width:600px;height:34px}
.hero-title{left:44px;top:62px;font-size:28px}
.hero-copy{left:44px;top:100px;width:540px;font-size:14.3px;line-height:16.4px;color:#f1f1f1}
.hero-copy p{margin-bottom:16.4px}

.photo{background:#999}
.photo-home{left:47px;top:313px;width:247px;height:164px;background:linear-gradient(160deg,#b4563c 0%,#9c7f66 45%,#7a8a4f 100%)}
.photo-office{left:311px;top:313px;width:247px;height:162px;background:linear-gradient(120deg,#c7b39c 0%,#8e8880 50%,#6d4a36 100%)}

.col-title{top:496px;font-size:25px}
.col-intro{top:543px;font-size:14.3px;line-height:16.4px}
.service-list{list-style:none;font-size:14.3px;line-height:16.4px}
.service-list li{position:relative;padding-left:19px}
.service-list li::before{content:"";position:absolute;left:5px;top:6px;width:5px;height:5px;background:var(--yellow)}

.home-col{left:51px}
.home-list{left:51px;top:592px;width:250px}
.insured-col{left:316px}
.insured-list{left:316px;top:576px;width:250px}

.quote-bar{left:0;top:853px;width:600px;height:56px;background:var(--charcoal)}
.quote-text{left:39px;top:866px;font-size:17.6px;color:#f1f1f1;white-space:nowrap;z-index:3}
.quote-text strong{font-weight:500;color:var(--charcoal)}
.slash{left:0;top:0;z-index:2}

/* Right spread */
.panel-right{left:600px;top:0;width:600px;height:928px;background:var(--white)}
.storage-title{left:644px;top:37px;font-size:27px}
.storage-col{top:86px}
.storage-col h3{font-weight:500;font-size:16.8px;color:var(--charcoal);margin-bottom:8px;line-height:1.2}
.storage-col p{font-size:14px;line-height:16.4px}
.col-household{left:642px;width:160px}
.col-commercial{left:818px;width:172px}
.col-mobile{left:1010px;width:170px}

.archive{left:600px;top:335px;width:600px;height:135px;background:linear-gradient(90deg,var(--yellow-deep) 0%,var(--yellow) 55%,#e8ad0e 100%)}
.archive-title{left:653px;top:352px;font-size:27px;color:var(--charcoal)}
.archive-copy{left:653px;top:382px;width:480px;font-size:14.3px;line-height:16.4px;color:var(--charcoal);font-weight:400}

.packing{left:600px;top:470px;width:600px;height:458px;background:var(--charcoal)}
.packing-title{left:655px;top:507px;font-size:27px}
.packing-copy{left:655px;top:549px;width:218px;font-size:14.3px;line-height:16.4px;color:#f1f1f1}
.packing-item{left:657px;width:520px;color:#f1f1f1;font-size:14.3px;line-height:16.4px}
.packing-item h4{font-weight:300;font-size:18.7px;color:var(--yellow);line-height:1.1;margin-bottom:1px}
.item-full{top:698px}
.item-part{top:769px}
.item-export{top:840px}
.family-photo{left:854px;top:481px;z-index:1}
</style>
</head>
<body>

<!-- Left spread -->
<div class="abs hero-photo" role="img" aria-label="Darkened photo of movers carrying boxes into a house"></div>
<svg class="abs hero-band" width="600" height="34" viewBox="0 0 600 34" aria-hidden="true">
  <rect width="600" height="34" fill="#2b2b2b"/>
  <polygon points="0,0 291,0 256,34 0,34" fill="var(--yellow)"/>
</svg>
<h1 class="abs display hero-title">Harbourside Removals and Storage</h1>
<div class="abs hero-copy">
  <p>Harbourside Removals and Storage provides seamless house removal and commercial business moves throughout the North west and nationwide.</p>
  <p>With more than two decades of experience within the moving and storage industry, Harbourside Removals and Storage provides a reliable, efficient service, ensuring our customers receive a quality service every time.</p>
  <p>In addition to our home, business and office removals we also provide other services such as storage solutions, packing services, antique and piano transportation.</p>
</div>

<div class="abs photo photo-home" role="img" aria-label="Photo of a couple unloading boxes from a removal van outside a brick house"></div>
<div class="abs photo photo-office" role="img" aria-label="Photo of an office with packed boxes, desks and empty shelving"></div>

<h2 class="abs display col-title home-col">Home removal services</h2>
<p class="abs col-intro home-col" style="width:240px">Our range of home removal services include …</p>
<ul class="abs service-list home-list">
  <li>Packing services</li>
  <li>Specialist antique and piano transportation</li>
  <li>Estate clearance service</li>
  <li>Removal and disposal of unwanted items</li>
  <li>Furniture dismantling and reassembly</li>
  <li>Export wrapping</li>
  <li>Storage</li>
  <li>Internal moves within your home</li>
  <li>Cleaning service</li>
  <li>Moving abroad</li>
</ul>

<h2 class="abs display col-title insured-col">Fully-insured movers</h2>
<p class="abs col-intro insured-col" style="width:260px">Other commercial services undertaken...</p>
<ul class="abs service-list insured-list">
  <li>Tower block relocation logistics</li>
  <li>multiple occupancy</li>
  <li>Crate rental</li>
  <li>Courier services</li>
  <li>Relocation of safes and heavy items (including lathes, large printers, commercial kitchens)</li>
  <li>Internal moves</li>
  <li>Transportation of confidential materials</li>
  <li>Storage</li>
  <li style="width:150px">Removal and disposal of unwanted items</li>
</ul>

<div class="abs quote-bar"></div>
<svg class="abs slash" width="600" height="928" viewBox="0 0 600 928" aria-hidden="true">
  <polygon points="488,754 599,754 541,928 422,928" fill="var(--yellow)" opacity="0.92"/>
</svg>
<p class="abs quote-text">Call us to arrange a free no obligation quotation on <strong>01632 960 214</strong></p>

<!-- Right spread -->
<div class="abs panel-right"></div>
<h2 class="abs display storage-title">Storage solutions</h2>
<div class="abs storage-col col-household">
  <h3>Household Storage</h3>
  <p>Harbourside Removals and Storage provides clean, dry secure storage for all your household furniture and goods. Our storage facilities are safe and secure with 24 hour CCTV and alarmed to give you peace of mind that your goods are safe with us.</p>
</div>
<div class="abs storage-col col-commercial">
  <h3>Commercial Storage</h3>
  <p>Harbourside Removals and Storage offers flexible storage solutions for businesses of all sizes, our services are tailor made to suit the changing needs of our customers. Our storage solutions are ideal for either long term or short term storage of stock, office equipment, palletised stock and archive storage.</p>
</div>
<div class="abs storage-col col-mobile">
  <h3>Mobile Self Storage</h3>
  <p>Mobile Self Storage is a convenient, hassle free, simple way to store your goods. We deliver a mobile storage unit directly to your home or business, you load your goods into the storage unit then we take it away to our storage facility and store it.</p>
</div>

<div class="abs archive" role="img" aria-label="Yellow-tinted photo of archive boxes on shelves"></div>
<h2 class="abs display archive-title">Archive Storage</h2>
<p class="abs archive-copy">Do you need an off-site archive solution to store your company’s files? Many company documents need to be stored for a number of years. Why have this burden, let us do it for you. We can deliver individual files and boxes at your request any time as and when you need them.</p>

<div class="abs packing"></div>
<svg class="abs family-photo" width="346" height="260" viewBox="0 0 346 260" role="img" aria-label="Photo of a smiling family sitting in front of moving boxes">
  <defs>
    <linearGradient id="familyTone" x1="0" y1="0" x2="1" y2="1">
      <stop offset="0" stop-color="#f3be22"/>
      <stop offset="0.55" stop-color="#c9a987"/>
      <stop offset="1" stop-color="#5a6f92"/>
    </linearGradient>
  </defs>
  <polygon points="0,0 346,0 346,200 270,260 80,217" fill="url(#familyTone)"/>
</svg>
<h2 class="abs display packing-title">Packing Service</h2>
<p class="abs packing-copy">Here at Harbourside Removals and Storage, we can assist you by providing a flexible packing service to suit your needs and budget, our range of packing services ensure you get the help you require, at a cost you’ll love</p>
<div class="abs packing-item item-full" style="width:380px">
  <h4>Full Packing Service</h4>
  <p>Leaving all your packing to us, we will come and pack your entire home ready for your move.</p>
</div>
<div class="abs packing-item item-part">
  <h4>Part Packing Service</h4>
  <p>Packing of breakables from crockery, precious glassware and ornaments, to your heavier items such as books, collectables and tools.</p>
</div>
<div class="abs packing-item item-export">
  <h4>Export Wrapping</h4>
  <p>We will export wrap selected items, such as antiques, paintings, pictures and high finish furniture for transport, local or long distance.</p>
</div>
<svg class="abs" style="left:1000px;top:900px" width="200" height="28" viewBox="0 0 200 28" aria-hidden="true">
  <polygon points="33,7 200,7 200,28 11,28" fill="var(--yellow)"/>
</svg>

</body>
</html>
```